1st Newsletter for KOBA - Online Gadgets seller.

KOBA - Kind Offers By All is a UK based online retailer selling various consumer electronics and gadgets, connecting international suppliers with customers from all over the world.
So far we were selling exclusively on Tradlo, so the newsletter will be targeted at our Tradlo customers, and needs to convert them to buy from our website instead.
We'd like the newsletter to have a warm, artistic and welcoming feel to it.
We opt for nice pastel colours, but any variations are welcome and will be considered.
We want the newsletter to go together with our website's look:
http://koba-shop.example

Industry/Entity Type

Electronics

```html
<!DOCTYPE html>
<html lang="en">
<head>
<meta charset="utf-8">
<title>KOBA – Newsletter</title>
<link href="https://fonts.googleapis.com/css2?family=Lato:wght@300;400;700;900&family=Noto+Serif:wght@400&family=Arimo:wght@400;700&display=swap" rel="stylesheet">
<style>
  :root {
    --ink: #333333;
    --text: #555555;
    --pink: #e5007d;
    --yellow: #ffd200;
    --dark-btn: #3a3a3a;
    --rule: #d6d6d6;
    --bg: #ffffff;
  }
  * { box-sizing: border-box; margin: 0; padding: 0; }
  html, body { width: 1200px; height: 2415px; overflow: hidden; background: var(--bg); }
  .newsletter { position: relative; width: 1200px; height: 2415px; }
  .abs { position: absolute; }

  .brand { left: 0; top: 28px; width: 1200px; text-align: center; }
  .brand-name {
    font-family: "Lato", sans-serif; font-weight: 900; font-size: 140px;
    color: var(--ink); letter-spacing: -4px; line-height: 1; display: inline-block;
  }

  .nav { left: 51px; top: 248px; font-family: "Lato", sans-serif; font-size: 27px; color: #222; }
  .nav span.sep { margin: 0 18px; }
  .social { left: 952px; top: 253px; display: flex; gap: 14px; }
  .social i { width: 24px; height: 24px; border-radius: 50%; background: #2b2b2b; display: block; }

  .hero { left: 51px; top: 307px; width: 1104px; height: 313px; background: linear-gradient(90deg, #8a8f94 0%, #a9adb1 55%, #d9dcde 80%, #eef0f1 100%); }
  .hero-photo { position: absolute; right: 0; top: 0; width: 560px; height: 313px;
    background: linear-gradient(90deg, rgba(200,203,206,0) 0%, #e4e6e8 45%, #f4f4f4 100%); }
  .hero-text { position: absolute; left: 28px; top: 62px; width: 560px;
    font-family: "Noto Serif", serif; font-size: 42px; line-height: 1.2; color: #3a3a3a; }
  .hero-text a { color: var(--yellow); text-decoration: underline; text-decoration-thickness: 2px; }

  .promo { top: 660px; font-family: "Noto Serif", serif; font-size: 32px; line-height: 1.2; color: var(--pink); text-align: center; white-space: nowrap; }
  .promo-delivery { left: 102px; width: 450px; }
  .promo-discount { left: 600px; width: 560px; }

  .rule { left: 26px; width: 1154px; height: 2px; background: var(--rule); }

  .product-title { font-family: "Arimo", sans-serif; font-weight: 700; font-size: 38px; line-height: 1.1; color: #222; width: 590px; }
  .product-price { font-family: "Arimo", sans-serif; font-weight: 700; font-size: 35px; color: var(--pink); }
  .product-desc { font-family: "Arimo", sans-serif; font-size: 24.5px; line-height: 41px; color: var(--text); width: 580px; }
  .btn { height: 80px; font-family: "Lato", sans-serif; font-size: 34px; display: flex; align-items: center; justify-content: center; text-transform: uppercase; }
  .btn-buy { background: var(--dark-btn); color: var(--yellow); width: 240px; }
  .btn-more { background: var(--yellow); color: #2a2a2a; width: 302px; }
</style>
</head>
<body>
<main class="newsletter">

  <header>
    <div class="abs brand"><span class="brand-name">koba</span></div>
    <nav class="abs nav">Home<span class="sep">-</span>Shop<span class="sep">-</span>About Us<span class="sep">-</span>Register</nav>
    <div class="abs social" aria-label="Social links"><i></i><i></i><i></i><i></i><i></i></div>
  </header>

  <section class="abs hero">
    <div class="hero-photo" role="img" aria-label="Photo of a person exhaling vapour from a white e-cigarette"></div>
    <p class="hero-text">We are your trusted Tradlo seller &amp; we invite you to our <a>new website!</a></p>
  </section>

  <p class="abs promo promo-delivery">Free UK Next Day Delivery<br>on all orders</p>
  <p class="abs promo promo-discount">Get 5% OFF your order! Discount<br>code: KOBA-NEW</p>

  <div class="abs rule" style="top:782px"></div>

  <div class="abs product-image" style="left:51px;top:830px;width:447px;height:448px;background:linear-gradient(90deg,#bdbdbd,#9ab6d9 30%,#555 60%,#d88ad6);opacity:.75" role="img" aria-label="Four clearomisers in grey, blue, black and pink with reflections"></div>
  <h2 class="abs product-title" style="left:583px;top:822px">CE5 Clearomiser / Atomizer For e-Cigarette</h2>
  <p class="abs product-price" style="left:583px;top:943px">£3.45</p>
  <p class="abs product-desc" style="left:583px;top:992px">orem ipsum dolor sit amet, consectetur adipiscing elit. Proin condimentum tellus pretium mattis faucibus. Fusce congue at quam eu fringilla.</p>
  <a class="abs btn btn-buy" style="left:585px;top:1175px">Buy Now</a>
  <a class="abs btn btn-more" style="left:843px;top:1175px">More Details</a>

  <div class="abs rule" style="top:1346px"></div>

  <h2 class="abs product-title" style="left:56px;top:1390px">eLiquid For e-Cigarette - Refill For CE4 CE5 ARO 10ml</h2>
  <p class="abs product-price" style="left:56px;top:1493px">£2.95</p>
  <p class="abs product-desc" style="left:56px;top:1555px">orem ipsum dolor sit amet, consectetur adipiscing elit. Proin condimentum tellus pretium mattis faucibus. Fusce congue at quam eu fringilla.</p>
  <a class="abs btn btn-buy" style="left:54px;top:1737px">Buy Now</a>
  <a class="abs btn btn-more" style="left:312px;top:1737px">More Details</a>
  <div class="abs product-image" style="left:703px;top:1392px;width:434px;height:422px;background:radial-gradient(circle at 50% 55%,#6f9a5a 0%,#c9d9b8 35%,#f4e6e6 60%,#ffffff 80%)" role="img" aria-label="E-liquid box surrounded by cherries, strawberry, mint, pipe and gumball flavour icons"></div>

  <div class="abs rule" style="top:1896px"></div>

  <div class="abs product-image" style="left:38px;top:2018px;width:460px;height:320px;background:linear-gradient(160deg,#f2f2f2 0%,#bdbdbd 40%,#2a2a2a 70%,#111 100%);border-radius:18px" role="img" aria-label="Black leather flip wallet case with a white phone"></div>
  <h2 class="abs product-title" style="left:583px;top:1940px">Leather Case Phone Cover Flip Wallet For Pomelo Fone 5 ……</h2>
  <p class="abs product-price" style="left:583px;top:2043px">£9.94</p>
  <p class="abs product-desc" style="left:583px;top:2108px">orem ipsum dolor sit amet, consectetur adipiscing elit. Proin condimentum tellus pretium mattis faucibus. Fusce congue at quam eu fringilla.</p>
  <a class="abs btn btn-buy" style="left:585px;top:2289px">Buy Now</a>
  <a class="abs btn btn-more" style="left:843px;top:2289px">More Details</a>

</main>
</body>
</html>
```